Rig up a website for a Rigging Company

We already have a logo. Looking for a website design that works on plinvara.com.
Our rigging company uses semi trucks, forklifts, and similar equipment to move large machines.
Our logo is white, black and red.

Target Market(s)

Medical Industry (moving medical equipment), Utility Industry (power equipment), Food Industry (moving bottling/packing equipment), US Government (large equipment)

Industry/Entity Type

It Company

Coding

Coded - Design and coding required

Number of Pages Required

5+ page

Font styles to use
Sans Serif

Colors
ec1f27
ffffff
0355a3

Requirements
Must have
• Home page, About page, Services Page, and Contact Information page
Nice to have
• Pictures of semi and forklifts and ability to insert our own pictures of our equipment

```html
<!DOCTYPE html>
<html lang="en">
<head>
<meta charset="utf-8">
<title>Corvell Rigging</title>
<link href="https://fonts.googleapis.com/css2?family=Archivo:wght@500;700;800&family=Lato:wght@400;700&display=swap" rel="stylesheet">
<style>
:root{
  --red:#ec1f27;
  --dark:#111111;
  --ink:#222222;
  --grey:#f1f1f1;
  --line:#dddddd;
  --white:#ffffff;
  --blue:#0355a3;
}
*{box-sizing:border-box;margin:0;padding:0}
html,body{width:1200px;height:2995px;overflow:hidden;background:var(--white)}
body{position:relative;font-family:'Lato',sans-serif;color:var(--ink)}
.abs{position:absolute}
h2.section-title{position:absolute;left:0;width:1200px;text-align:center;font-family:'Archivo',sans-serif;font-weight:700;font-size:32px;color:var(--dark);letter-spacing:.5px}
.rule{position:absolute;left:530px;width:140px;height:7px;border-top:2px solid var(--red);border-bottom:2px solid var(--red)}

/* header */
.brand{position:absolute;left:100px;top:22px;font-family:'Archivo',sans-serif;font-weight:800;font-size:46px;line-height:1;color:var(--dark);letter-spacing:-1px}
.brand-sub{position:absolute;left:176px;top:76px;font-family:'Archivo',sans-serif;font-weight:800;font-size:26px;color:var(--dark);letter-spacing:1px}
.top-contact{position:absolute;top:22px;display:flex;gap:12px;align-items:flex-start;font-size:14px;color:#444;line-height:1.4}
.top-contact svg{margin-top:2px}
.nav{position:absolute;left:410px;top:84px;width:790px;height:40px;background:var(--red);clip-path:polygon(14px 0,100% 0,100% 100%,0 100%)}
.nav a{position:absolute;top:11px;color:var(--white);font-family:'Archivo',sans-serif;font-weight:700;font-size:14px;text-decoration:none;letter-spacing:.3px}
.nav .sep{position:absolute;top:10px;width:1px;height:20px;background:rgba(255,255,255,.45)}

/* hero */
.hero{position:absolute;left:0;top:124px;width:1200px;height:600px;background:linear-gradient(180deg,#5d7a94 0%,#b58a6a 55%,#e5a163 72%,#3b3d44 100%)}
.hero h1{position:absolute;left:0;width:1200px;top:656px;text-align:center;font-family:'Archivo',sans-serif;font-weight:700;font-size:40px;color:var(--white)}
.hero-arrow{position:absolute;top:390px;width:26px;height:40px;background:rgba(255,255,255,.85);display:flex;align-items:center;justify-content:center}

/* welcome */
.welcome-title{position:absolute;left:100px;top:786px;font-family:'Archivo',sans-serif;font-weight:800;font-size:32px;color:var(--dark)}
.welcome-title span{color:var(--red)}
.lead{position:absolute;left:100px;top:870px;width:630px;font-weight:700;font-size:12.5px;line-height:1.6;color:var(--dark)}
.body-copy{position:absolute;left:100px;top:922px;width:630px;font-size:12.5px;line-height:1.75;color:#333}
.btn{position:absolute;background:var(--red);color:var(--white);border-radius:20px;font-family:'Archivo',sans-serif;font-weight:700;display:flex;align-items:center;gap:10px}
.btn i{width:22px;height:22px;border-radius:50%;background:var(--white);display:flex;align-items:center;justify-content:center}
.video{position:absolute;left:770px;top:780px;width:330px;height:250px;background:linear-gradient(180deg,#7fb0dc 0%,#c9d8e4 55%,#56524e 80%,#3a4652 100%)}
.video-bar{position:absolute;left:770px;top:1010px;width:330px;height:20px;background:#eeeeee;border-top:1px solid #ccc}
.video-bar .fill{position:absolute;left:24px;top:8px;width:170px;height:4px;background:var(--red)}
.video-bar .track{position:absolute;left:194px;top:8px;width:80px;height:4px;background:#bbb}
.watch{position:absolute;left:770px;top:1058px;font-size:13px;color:#333}

/* services */
.band-grey{position:absolute;left:0;width:1200px;background:var(--grey)}
.card{position:absolute;top:1268px;width:230px;height:248px;background:var(--white)}
.card .photo{height:190px}
.card .label{position:absolute;left:0;top:190px;width:230px;height:58px;border-top:4px solid var(--red)}
.card .icon{position:absolute;left:0;top:0;width:54px;height:54px;background:var(--red);display:flex;align-items:center;justify-content:center}
.card .name{position:absolute;left:68px;top:10px;font-family:'Archivo',sans-serif;font-weight:500;font-size:14.5px;line-height:1.25;color:var(--dark)}

/* projects */
.proj{position:absolute;top:1748px;height:198px}
.proj-feature{position:absolute;left:420px;top:1728px;width:368px;height:262px;background:linear-gradient(180deg,#6b0e12 0%,#d7383a 50%,#f6b19a 66%,#7a1414 100%)}
.proj-caption{position:absolute;left:420px;top:1946px;width:368px;height:44px;background:rgba(0,0,0,.72);color:var(--white);text-align:center;font-family:'Archivo',sans-serif;font-weight:500;font-size:19px;line-height:44px}
.side-arrow{position:absolute;width:24px;height:36px;background:#222;display:flex;align-items:center;justify-content:center}

/* customers */
.client{position:absolute;top:2200px;width:180px;height:100px;background:var(--white);border:1px solid #d4d4d4;display:flex;align-items:center;justify-content:center;gap:8px;font-family:'Archivo',sans-serif;font-weight:700;font-size:24px;color:var(--blue)}
.client b{width:16px;height:16px;border-radius:50%;background:var(--blue)}

/* inquiry */
.inq-title{position:absolute;left:100px;top:2420px;font-family:'Archivo',sans-serif;font-weight:700;font-size:32px;color:var(--dark)}
.inq-text{position:absolute;left:100px;top:2490px;width:330px;font-size:12.5px;line-height:1.85;color:#333}
.inq-text span{color:var(--red)}
.form-head{position:absolute;left:460px;top:2424px;font-size:14px;color:#333}
.field{position:absolute;width:308px;height:44px;border:1px solid var(--line);font-size:12px;color:#555;padding:14px 16px}

/* footer */
.footer{position:absolute;left:0;top:2678px;width:1200px;height:272px;background:var(--dark)}
.f-head{position:absolute;top:2712px;font-family:'Archivo',sans-serif;font-weight:700;font-size:18px;color:var(--white)}
.f-head span{color:var(--red)}
.f-rule{position:absolute;top:2744px;height:2px;background:#555}
.f-rule::after{content:"";position:absolute;right:-4px;top:-3px;width:8px;height:8px;border-radius:50%;background:var(--red)}
.f-links{position:absolute;left:100px;top:2764px;list-style:none}
.f-links li{height:42px;font-size:13px;color:var(--white);display:flex;align-items:center;gap:12px}
.f-links li.on{color:var(--red)}
.f-links li::before{content:"›";color:var(--red);font-size:18px;line-height:1}
.f-col{position:absolute;width:1px;background:#333;top:2712px;height:200px}
.f-contact{position:absolute;left:300px;top:2764px;font-size:13px;color:var(--white);line-height:1.3}
.f-contact .row{display:flex;gap:12px;align-items:flex-start;margin-bottom:16px}
.f-contact svg{flex:none;margin-top:1px}
.f-social{position:absolute;left:588px;top:2764px;list-style:none}
.f-social li{height:38px;display:flex;align-items:center;gap:12px;font-family:'Archivo',sans-serif;font-weight:700;font-size:12px;color:var(--white)}
.f-social li b{width:24px;height:24px;border-radius:50%;background:var(--red)}
.f-brand{position:absolute;left:808px;top:2766px;font-family:'Archivo',sans-serif;font-weight:800;font-size:52px;line-height:1;color:var(--white);letter-spacing:-1px}
.f-brand-sub{position:absolute;left:876px;top:2826px;font-family:'Archivo',sans-serif;font-weight:800;font-size:26px;color:var(--white);letter-spacing:2px}
.copyright{position:absolute;left:0;top:2950px;width:1200px;height:45px;background:var(--red);color:var(--white);text-align:center;font-size:13px;line-height:45px}
</style>
</head>
<body>

<header>
  <div class="brand">Corvell</div>
  <div class="brand-sub">RIGGING</div>

  <div class="top-contact" style="left:758px">
    <svg width="24" height="24" viewBox="0 0 24 24"><path d="M6 3l4 4-2 3c1 2 4 5 6 6l3-2 4 4-3 3C10 21 3 14 3 6z" fill="none" stroke="#ec1f27" stroke-width="2"/></svg>
    <div>Call Us:<br>123 456 7890</div>
  </div>
  <div class="top-contact" style="left:902px">
    <svg width="28" height="24" viewBox="0 0 28 24"><rect x="2" y="4" width="24" height="16" fill="none" stroke="#ec1f27" stroke-width="2"/><path d="M2 4l12 9 12-9" fill="none" stroke="#ec1f27" stroke-width="2"/></svg>
    <div>Mail Us:<br>inquiry@plinvara.com</div>
  </div>

  <nav class="nav">
    <a style="left:72px">HOME</a>
    <span class="sep" style="left:188px"></span>
    <a style="left:214px">ABOUT US</a>
    <span class="sep" style="left:352px"></span>
    <a style="left:390px">OUR SERVICES</a>
    <span class="sep" style="left:550px"></span>
    <a style="left:594px">CONTACT US</a>
  </nav>
</header>

<section>
  <div class="hero" role="img" aria-label="Crane lifting a jet aircraft on a ship deck at sunset with crew"></div>
  <div class="hero-arrow" style="left:0"><svg width="10" height="16"><path d="M8 2L2 8l6 6" fill="none" stroke="#222" stroke-width="2"/></svg></div>
  <div class="hero-arrow" style="left:1174px"><svg width="10" height="16"><path d="M2 2l6 6-6 6" fill="none" stroke="#222" stroke-width="2"/></svg></div>
  <h1 class="hero-title" style="position:absolute;left:0;top:656px;width:1200px;text-align:center;font-family:'Archivo',sans-serif;font-weight:700;font-size:40px;color:#fff">On Time And Affordable Rigging Services</h1>
</section>

<section>
  <h2 class="welcome-title">WELCOME TO <span>CORVELL</span></h2>
  <p class="lead">Lorem ipsum dolor sit amet, consectetuer adipiscing elit, sed diam nonummy nibh euismod tincidunterr uter laoreet dolore magna aliquam erat volutpat. Ut wisi enim ad minim veniam, quis nostrud exe</p>
  <p class="body-copy">Lorem ipsum dolor sit amet, consectetuer adipiscing elit, sed diam nonummy nibh euismod tincidunt utwi laoreet dolore magna aliquam erat volutpat. Ut wisi enim ad minim veniam, quis nostrud exerci tationwer ullamcorper suscipit lobortis nisl ut aliquip ex ea commodo consequat. Duis autem vel eum iriure dolor in et accumsan et iusto odio dignissim qui blandit praesent luptatum zzril delenit augue duis dolore te werri feugait nulla facilisi.</p>
  <div class="btn" style="left:100px;top:1048px;height:36px;padding:0 8px 0 14px;font-size:13px">READ MORE <i><svg width="8" height="10"><path d="M2 1l4 4-4 4" fill="none" stroke="#ec1f27" stroke-width="2"/></svg></i></div>

  <div class="video" role="img" aria-label="Video still of a crawler crane beside a moored barge"></div>
  <div class="video-bar"><span class="fill"></span><span class="track"></span></div>
  <svg class="abs" style="left:742px;top:1022px" width="26" height="44" viewBox="0 0 26 44"><path d="M22 40C8 36 4 22 10 4" fill="none" stroke="#ec1f27" stroke-width="2"/><path d="M5 9l5-6 4 7" fill="none" stroke="#ec1f27" stroke-width="2"/></svg>
  <p class="watch">Watch Our Video</p>
</section>

<section>
  <div class="band-grey" style="top:1132px;height:446px"></div>
  <h2 class="section-title" style="top:1170px">OUR SERVICES</h2>
  <div class="rule" style="top:1218px"></div>

  <div class="card" style="left:100px">
    <div class="photo" role="img" aria-label="Large medical scanner on lifting skates" style="background:linear-gradient(180deg,#8a6a58,#b23a3a 60%,#6d5a4c)"></div>
    <div class="label"><span class="icon"><svg width="28" height="28"><rect x="4" y="14" width="20" height="10" fill="#fff"/><rect x="10" y="4" width="8" height="8" fill="#fff"/></svg></span><span class="name">MOVING MEDICAL<br>EQUIPMENT</span></div>
  </div>
  <div class="card" style="left:356px">
    <div class="photo" role="img" aria-label="Power transformer on a heavy trailer" style="background:linear-gradient(180deg,#4f8fd0,#9cb6cc 45%,#5b4a44 80%)"></div>
    <div class="label"><span class="icon"><svg width="28" height="28"><rect x="4" y="8" width="20" height="14" fill="#fff"/><rect x="8" y="12" width="12" height="6" fill="#ec1f27"/></svg></span><span class="name">MOVING POWER<br>EQUIPMENT</span></div>
  </div>
  <div class="card" style="left:612px">
    <div class="photo" role="img" aria-label="Packing machinery lifted by crane beside a city skyline" style="background:linear-gradient(180deg,#5d87b4,#a9b8c4 55%,#3f4348)"></div>
    <div class="label"><span class="icon"><svg width="28" height="28"><rect x="4" y="14" width="9" height="9" fill="#fff"/><rect x="15" y="14" width="9" height="9" fill="#fff"/><rect x="9" y="4" width="10" height="9" fill="#fff"/></svg></span><span class="name">MOVING PACKING<br>EQUIPMENT</span></div>
  </div>
  <div class="card" style="left:870px">
    <div class="photo" role="img" aria-label="Large wrapped equipment hoisted by crane" style="background:linear-gradient(180deg,#3f78c4,#7fa7d6 50%,#4f6e8e)"></div>
    <div class="label"><span class="icon"><svg width="28" height="28"><path d="M6 24V6h14" fill="none" stroke="#fff" stroke-width="3"/><rect x="14" y="14" width="10" height="10" fill="#fff"/></svg></span><span class="name">MOVING LARGE<br>EQUIPMENT</span></div>
  </div>
</section>

<section>
  <h2 class="section-title" style="top:1636px">RECENT PROJECTS</h2>
  <div class="rule" style="top:1684px"></div>

  <div class="proj" role="img" aria-label="Crane lifting a jet on a ship deck" style="left:0;width:275px;background:linear-gradient(180deg,#6e8fb0,#c79a7a 60%,#3a3a3e)"></div>
  <div class="proj" role="img" aria-label="Cylindrical tank rigged to a crane" style="left:275px;width:145px;background:linear-gradient(180deg,#6f9fd6,#c7ccd0 65%,#7b7f84)"></div>
  <div class="proj-feature" role="img" aria-label="Construction crane silhouettes against a red sunset"></div>
  <div class="proj-caption">LOREM IPSUM DUIS AUTE IRURE</div>
  <div class="proj" role="img" aria-label="Tower crane among city buildings" style="left:788px;width:137px;background:linear-gradient(180deg,#9fb4c6,#c9c2a6 60%,#6b6b6b)"></div>
  <div class="proj" role="img" aria-label="Crawler crane lifting a barge at a harbour" style="left:925px;width:275px;background:linear-gradient(180deg,#6ea4d8,#c7d8e6 55%,#4b4a48)"></div>
  <div class="side-arrow" style="left:0;top:1830px"><svg width="10" height="14"><path d="M7 2L2 7l5 5" fill="none" stroke="#fff" stroke-width="2"/></svg></div>
  <div class="side-arrow" style="left:1176px;top:1830px"><svg width="10" height="14"><path d="M3 2l5 5-5 5" fill="none" stroke="#fff" stroke-width="2"/></svg></div>
</section>

<section>
  <div class="band-grey" style="top:2058px;height:300px"></div>
  <h2 class="section-title" style="top:2102px">OUR CUSTOMERS</h2>
  <div class="rule" style="top:2150px"></div>
  <svg class="abs" style="left:58px;top:2226px" width="20" height="46"><path d="M18 2L4 23l14 21" fill="none" stroke="#888" stroke-width="2"/></svg>
  <div class="client" style="left:96px"><b></b>Norvane</div>
  <div class="client" style="left:302px"><b></b>Talbrook</div>
  <div class="client" style="left:508px"><b></b>Aventra</div>
  <div class="client" style="left:714px"><b></b>Solvix</div>
  <div class="client" style="left:920px"><b></b>Ketterly</div>
  <svg class="abs" style="left:1116px;top:2226px" width="20" height="46"><path d="M2 2l14 21L2 44" fill="none" stroke="#ec1f27" stroke-width="2"/></svg>
</section>

<section>
  <h2 class="inq-title">QUICK INQUIRY</h2>
  <p class="inq-text">Duis autem vel eum iriure dolormi opl inmoklerri erer hendi rerit in vulpu tateml velitm essemol mower weri molestiel conseqb uat, velmi illum dolor eokf noewerr atnrhendi rerit in vulpu tateml velitm essemol moweri weri nulla more facilisis... <span>[+]</span></p>
  <p class="form-head">Please Fill Up Bellow Form</p>
  <div class="field" style="left:460px;top:2460px">Name</div>
  <div class="field" style="left:792px;top:2460px">Email</div>
  <div class="field" style="left:460px;top:2512px">Phone</div>
  <div class="field" style="left:792px;top:2512px">Message</div>
  <div class="btn" style="left:460px;top:2566px;height:44px;padding:0 10px 0 18px;font-size:24px;font-weight:500">Submit <i><svg width="8" height="10"><path d="M2 1l4 4-4 4" fill="none" stroke="#ec1f27" stroke-width="2"/></svg></i></div>
</section>

<footer>
  <div class="footer"></div>

  <h3 class="f-head" style="left:100px">Quick <span>Links</span></h3>
  <div class="f-rule" style="left:100px;width:118px"></div>
  <ul class="f-links">
    <li class="on">Home</li>
    <li>About Us</li>
    <li>Our Services</li>
    <li>Contact Us</li>
  </ul>
  <div class="f-col" style="left:262px"></div>

  <h3 class="f-head" style="left:300px">Contact <span>Details</span></h3>
  <div class="f-rule" style="left:300px;width:202px"></div>
  <div class="f-contact">
    <div class="row"><svg width="14" height="18"><path d="M7 17C2 10 1 8 1 6a6 6 0 0 1 12 0c0 2-1 4-6 11z" fill="#ec1f27"/><circle cx="7" cy="6" r="2" fill="#111"/></svg><div><b>Corvell Rigging</b><br>Lorem ipsum dolor sit amet,<br>consectetuer adipiscing</div></div>
    <div class="row"><svg width="14" height="14" viewBox="0 0 24 24"><path d="M6 3l4 4-2 3c1 2 4 5 6 6l3-2 4 4-3 3C10 21 3 14 3 6z" fill="#ec1f27"/></svg>123 456 7890</div>
    <div class="row"><svg width="14" height="14" viewBox="0 0 24 24"><path d="M6 3l4 4-2 3c1 2 4 5 6 6l3-2 4 4-3 3C10 21 3 14 3 6z" fill="#ec1f27"/></svg>123 456 7890</div>
    <div class="row"><svg width="16" height="12"><rect x="0" y="0" width="16" height="12" fill="#ec1f27"/><path d="M0 0l8 6 8-6" fill="none" stroke="#111" stroke-width="1.5"/></svg>inquiry@plinvara.com</div>
  </div>
  <div class="f-col" style="left:546px"></div>

  <h3 class="f-head" style="left:586px">Follow <span>Us</span></h3>
  <div class="f-rule" style="left:586px;width:138px"></div>
  <ul class="f-social">
    <li><b></b>FRIENDLANE</li>
    <li><b></b>CHIRPLINE</li>
    <li><b></b>WORKMESH</li>
    <li><b></b>CIRCLEPLUS</li>
  </ul>

  <div class="f-brand">Corvell</div>
  <div class="f-brand-sub">RIGGING</div>

  <div class="copyright">Copyright © 2017 Corvell Rigging. All Rights Reserved.</div>
</footer>

</body>
</html>
```